Fennick Executive Search - New Business Card Design Project

We are an executive search firm called Fennick Executive Search based in the UK. We require a custom design for a business card. We're looking to convey a professional service to executives for executive search recruitment services. In terms of colours, we like dark blues and grays (maybe even silver incorporated somewhere if we go for a foiled type of card) but we're open to your artistic flare. See our current logo in attachments. We are totally open on design so long as the design is slick and professional.
Updates

Thanks for all your contributions of various designs. I have to say the quality of work has been amazing which is going to make our job quite difficult in the coming days on making a decision. Thanks to you all that have taken the time to submit designs thus far. We'll keep on reviewing and try to narrow down our selection as soon as possible.

Target Market(s)

Executive Search

Industry/Entity Type

Recruitment

Contact Information for Business Card

Fennick Executive Search,
Exclusively Sourcing & Hiring Senior Leaders
Gordon Pellbury, Managing Director,
07823 906417
0117 486 7132
gordon@fennickexecutive.co.uk
fennickexecutive.co.uk
58 Lindmoor Court, Hatherley Road, Bristol, BS32 9QJ

Font styles to use
Sans Serif
Other font styles liked:
• Roboto (which is used in our logo)

Requirements
Must have
• Our logo (It has a subtle fade on it from #02071d at top to #333649 at bottom)
• The logo can be on one side or both sides
• Must be elegant and professional
• We have 2nd slogan CONSULT | INSPIRE | INNOVATE | DELIVER which can be incorporated into the card
Nice to have
• Use of blues and grey colours
• Compatible with similar styling to our website fennickexecutive.co.uk
Should not have
• Must not be overly brash
• Must not contain cartoon characters

```html
<!DOCTYPE html>
<html lang="en">
<head>
<meta charset="utf-8">
<title>Fennick Executive Search – Business Card</title>
<link href="https://fonts.googleapis.com/css2?family=Roboto:wght@400;500;700&display=swap" rel="stylesheet">
<style>
  :root {
    --page-bg: #e4e4e4;
    --navy-top: #0b1024;
    --navy-bottom: #2c3148;
    --navy: #131935;
    --card-light: #efefef;
    --accent-blue: #3d6db5;
    --text-white: #ffffff;
    --text-grey: #4a4d57;
    --icon-grey: #8d909a;
  }
  * { box-sizing: border-box; margin: 0; padding: 0; }
  html, body {
    width: 1200px; height: 960px; overflow: hidden;
    background: var(--page-bg);
    font-family: "Roboto", Arial, sans-serif;
  }
  .card {
    position: absolute; left: 280px;
    width: 640px; height: 400px;
    overflow: hidden;
    box-shadow: 0 6px 18px rgba(0,0,0,0.18);
  }
  /* Front */
  .card-front {
    top: 60px;
    background: linear-gradient(180deg, var(--navy-top) 0%, var(--navy-bottom) 100%);
  }
  .front-brand {
    position: absolute; left: 120px; top: 110px;
    color: var(--text-white); font-weight: 700;
    font-size: 40px; line-height: 1.02; letter-spacing: 0.5px;
    text-transform: uppercase;
  }
  .front-tagline {
    position: absolute; left: 122px; top: 206px;
    color: var(--accent-blue); font-size: 20px; font-weight: 400;
  }
  .front-slogan {
    position: absolute; left: 0; right: 0; top: 322px;
    text-align: center;
    color: var(--accent-blue); font-size: 19px; letter-spacing: 0.6px;
  }
  /* Back */
  .card-back {
    top: 500px;
    background: var(--card-light);
  }
  .back-logo {
    position: absolute; right: 34px; top: 36px;
    display: flex; align-items: center; gap: 12px;
  }
  .back-logo-square {
    width: 46px; height: 46px;
    background: linear-gradient(180deg, #02071d 0%, #333649 100%);
  }
  .back-logo-name {
    color: var(--navy); font-weight: 700; font-size: 16px;
    line-height: 1.15; text-transform: uppercase;
  }
  .person {
    position: absolute; left: 52px; top: 160px;
  }
  .person-name {
    color: var(--navy); font-weight: 700; font-size: 31px;
  }
  .person-title {
    color: var(--text-grey); font-size: 20px; margin-top: 2px;
  }
  .contact-band {
    position: absolute; left: 0; right: 0; bottom: 0; height: 112px;
    background: var(--navy);
    color: var(--text-white); font-size: 14.5px; line-height: 1.45;
  }
  .contact-group {
    position: absolute; top: 24px;
    display: grid; grid-template-columns: 22px auto; column-gap: 12px; row-gap: 4px;
    align-items: start;
  }
  .contact-group.left { left: 52px; }
  .contact-group.right { left: 360px; }
  .icon { width: 15px; height: 15px; margin-top: 3px; fill: var(--icon-grey); }
  .icon-stroke { fill: none; stroke: var(--icon-grey); stroke-width: 1.6; }
</style>
</head>
<body>

<section class="card card-front" aria-label="Business card front">
  <div class="front-brand">Fennick<br>Executive Search</div>
  <div class="front-tagline">Exclusively Sourcing &amp; Hiring Senior Leaders</div>
  <div class="front-slogan">CONSULT | INSPIRE | INNOVATE | DELIVER</div>
</section>

<section class="card card-back" aria-label="Business card back">
  <div class="back-logo">
    <div class="back-logo-square"></div>
    <div class="back-logo-name">Fennick<br>Executive Search</div>
  </div>

  <div class="person">
    <div class="person-name">Gordon Pellbury</div>
    <div class="person-title">Managing Director</div>
  </div>

  <div class="contact-band">
    <div class="contact-group left">
      <svg class="icon" viewBox="0 0 16 16" aria-hidden="true"><path d="M3.2 1.5l2.3 2.6-1.3 1.7c.9 2 2.4 3.5 4.4 4.4l1.7-1.3 2.6 2.3-1.2 2.2C6.5 13.6 2.4 9.5 1 4.5z"/></svg>
      <div>07823 906417<br>0117 486 7132</div>
      <svg class="icon" viewBox="0 0 16 16" aria-hidden="true"><rect class="icon-stroke" x="1.5" y="3.5" width="13" height="9"/><path class="icon-stroke" d="M1.5 3.5l6.5 5 6.5-5"/></svg>
      <div>gordon@fennickexecutive.co.uk</div>
    </div>
    <div class="contact-group right">
      <svg class="icon" viewBox="0 0 16 16" aria-hidden="true"><circle class="icon-stroke" cx="8" cy="8" r="6.3"/><ellipse class="icon-stroke" cx="8" cy="8" rx="2.8" ry="6.3"/><path class="icon-stroke" d="M1.7 8h12.6"/></svg>
      <div>fennickexecutive.co.uk</div>
      <svg class="icon" viewBox="0 0 16 16" aria-hidden="true"><path d="M8 1a4.8 4.8 0 0 0-4.8 4.8C3.2 9.4 8 15 8 15s4.8-5.6 4.8-9.2A4.8 4.8 0 0 0 8 1zm0 6.6a1.8 1.8 0 1 1 0-3.6 1.8 1.8 0 0 1 0 3.6z"/></svg>
      <div>58 Lindmoor Court, Hatherley Road<br>Bristol, BS32 9QJ</div>
    </div>
  </div>
</section>

</body>
</html>
```